New Law Firm needs a business card design

I need a business card for my new law firm called Fenwick Estates and Trusts. I would like designs to use my logo attached. My firm is new and modern. I like the colors orange, white, grey and black. The design I will chose will be one which uses color well, one which looks impressive, smart and modern.

Target Market(s)

Adults aged 30 to 50 seeking professional advice.

Industry/Entity Type

Law Firm

Requirements
Must have
• My logo which is attached.

Must have a modern font, similar to my logo and draft business card.
Should not have
• Any symbols about law, such as scales etc.

```html
<!DOCTYPE html>
<html lang="en">
<head>
<meta charset="utf-8">
<title>Fenwick Estates and Trusts – Business Card</title>
<link rel="stylesheet" href="https://fonts.googleapis.com/css2?family=Open+Sans:wght@400;600;700&display=swap">
<style>
  :root {
    --page-bg: #e9e7e4;
    --card-dark: #333333;
    --card-light: #f4f4f4;
    --accent: #e8961e;
    --text-light: #ffffff;
    --text-soft: #e6e6e6;
    --brand-grey: #6b6b6b;
  }
  * { margin: 0; padding: 0; box-sizing: border-box; }
  html, body {
    width: 1200px; height: 900px; overflow: hidden;
    background: var(--page-bg);
    font-family: "Open Sans", Arial, sans-serif;
  }
  .canvas { position: relative; width: 1200px; height: 900px; }
  .card {
    position: absolute; left: 370px; width: 455px; height: 278px;
    background: var(--card-dark); overflow: hidden;
    box-shadow: 0 2px 6px rgba(0,0,0,0.25);
    color: var(--text-light);
  }
  .card--front { top: 154px; }
  .card--back { top: 463px; }

  .light-panel { position: absolute; top: 0; height: 278px; width: 220px; background: var(--card-light); }
  .card--front .light-panel { left: 0; border-radius: 0 139px 139px 0; }
  .card--back .light-panel { right: 0; width: 225px; border-radius: 139px 0 0 139px; }

  .accent-rule { position: absolute; height: 4px; background: var(--accent); }
  .card--front .accent-rule { top: 192px; left: 210px; right: 0; }
  .card--back .accent-rule { top: 192px; left: 0; width: 245px; }

  .brand-name {
    position: absolute; color: var(--brand-grey);
    font-weight: 400; font-size: 15px; line-height: 1.25;
    letter-spacing: 2px; text-transform: uppercase;
  }
  .card--front .brand-name { left: 16px; top: 112px; }
  .card--back .brand-name { left: 250px; top: 118px; }

  .person { position: absolute; left: 225px; top: 36px; }
  .person__name { font-size: 18px; font-weight: 700; }
  .person__role {
    font-size: 14px; font-weight: 400; margin-left: 4px; padding-left: 6px;
    border-left: 2px solid var(--accent);
  }
  .person__degrees { font-family: Arial, sans-serif; font-size: 10.5px; color: var(--text-soft); margin-top: 4px; }

  .contact-list { position: absolute; left: 240px; top: 106px; list-style: none; }
  .contact-list li { display: flex; align-items: center; height: 23px; font-size: 11.5px; }
  .contact-list svg { width: 12px; height: 12px; margin-right: 14px; fill: var(--accent); }

  .office { position: absolute; left: 225px; top: 218px; font-size: 11px; line-height: 1.45; }
  .office__name { font-weight: 700; }

  .services {
    position: absolute; right: 247px; top: 78px; list-style: none;
    text-align: right; font-size: 14px; line-height: 22px;
  }
  .disclaimer { position: absolute; left: 29px; top: 220px; font-size: 11px; line-height: 1.45; }
</style>
</head>
<body>
<main class="canvas">
  <section class="card card--front" aria-label="Business card front">
    <div class="light-panel"></div>
    <p class="brand-name">Fenwick<br>Estates and<br>Trusts</p>
    <div class="person">
      <p><span class="person__name">Daniel Marsh</span><span class="person__role">LAWYER</span></p>
      <p class="person__degrees">Assoc.Deg.Law, BLJSt, LLB, Grad Dip Law.</p>
    </div>
    <ul class="contact-list">
      <li><svg viewBox="0 0 24 24" aria-hidden="true"><path d="M6.6 10.8a15.1 15.1 0 0 0 6.6 6.6l2.2-2.2a1 1 0 0 1 1-.25 11.4 11.4 0 0 0 3.6.57 1 1 0 0 1 1 1V20a1 1 0 0 1-1 1A17 17 0 0 1 3 4a1 1 0 0 1 1-1h3.5a1 1 0 0 1 1 1c0 1.25.2 2.45.57 3.57a1 1 0 0 1-.25 1z"/></svg>+1 555.210.4400</li>
      <li><svg viewBox="0 0 24 24" aria-hidden="true"><path d="M7 3h10v5H7zM4 9h16a2 2 0 0 1 2 2v6h-4v4H6v-4H2v-6a2 2 0 0 1 2-2zm4 7v3h8v-3z"/></svg>+1 555.210.4401</li>
      <li><svg viewBox="0 0 24 24" aria-hidden="true"><path d="M2 5h20v14H2zm2 2v.5l8 5 8-5V7l-8 5z"/></svg>daniel@fenwicktrusts.com.au</li>
    </ul>
    <div class="accent-rule"></div>
    <div class="office">
      <p class="office__name">Fenwick Estates and Trusts</p>
      <p>Streetname 123, State ZIP code 123456</p>
    </div>
  </section>

  <section class="card card--back" aria-label="Business card back">
    <div class="light-panel"></div>
    <ul class="services">
      <li>Wills</li>
      <li>Powers of Attorney</li>
      <li>Deceased Estates</li>
      <li>Will Disputes</li>
    </ul>
    <p class="brand-name">Fenwick<br>Estates and<br>Trusts</p>
    <div class="accent-rule"></div>
    <p class="disclaimer">Liability limited by a scheme approved<br>under professional standards legislation.</p>
  </section>
</main>
</body>
</html>
```